Exciting new branding of Recruitment Company based on it's new website

We have an exciting new website we are about to launch and would like to have letterhead, business cards, email signature options, email banner, linkedin and facebook cover images all refreshed to match the website. I have attached the existing logo. The website is at http://brightcrewhire.samplehost.com/ and we are particularly interested in the grey with orange writing at the base of the first page where it says Register Now

Target Market(s)

Recruitment

Contact Information for Business Card

Dana Holt
Account Executive
T: 1300 582 317
M: 0412 637 845
E: dana@brightcrewhire.com.au
W: brightcrewhire.com.au
A: Suite 3, 42 Tamsin Court, Deakin ACT 2600
ABN: 52 418 736 904

Font styles to use
Serif
Sans Serif

Requirements
Must have
• The grey colour from the website

```html
<!DOCTYPE html>
<html lang="en">
<head>
<meta charset="utf-8">
<title>Bright Crew Hire — Stationery</title>
<link rel="stylesheet" href="https://fonts.googleapis.com/css2?family=Lato:ital,wght@0,400;0,700;0,900;1,400&display=swap">
<style>
  :root {
    --orange: #f39a1e;
    --grey: #a9aaa6;
    --text-grey: #5d5d5d;
    --rule-red: #e58a7a;
    --card-dark: #1f1f1d;
    --paper: #ffffff;
    --backdrop: #e9e6e5;
  }
  * { box-sizing: border-box; margin: 0; padding: 0; }
  html, body { width: 763px; height: 1200px; overflow: hidden; }
  body {
    background: var(--backdrop);
    font-family: "Lato", Arial, sans-serif;
    color: var(--text-grey);
    position: relative;
  }

  /* Letterhead */
  .letterhead {
    position: absolute; left: 181px; top: 24px;
    width: 400px; height: 566px;
    background: var(--paper);
    box-shadow: 0 2px 8px rgba(0,0,0,.12);
    overflow: hidden;
  }
  .letterhead__brand {
    position: absolute; left: 36px; top: 34px;
    font-weight: 900; font-size: 17px; line-height: 1;
    color: var(--orange);
  }
  .letterhead__contact {
    position: absolute; right: 30px; top: 30px;
    text-align: right; font-size: 6.5px; line-height: 1.55;
    font-style: normal; color: var(--text-grey);
  }
  .letterhead__contact .abn { color: var(--orange); }
  .letterhead__body {
    position: absolute; left: 36px; top: 104px; width: 318px;
    font-style: italic; font-size: 7.4px; line-height: 1.6;
    color: var(--text-grey);
  }
  .letterhead__body p { margin-bottom: 9px; }
  .letterhead__signoff { margin-top: 14px; }
  .letterhead__signature {
    display: block; width: 34px; height: 14px; margin-top: 8px;
    background: linear-gradient(90deg, rgba(243,154,30,.35), rgba(243,154,30,.15));
    border-radius: 3px;
  }
  .letterhead__footer {
    position: absolute; left: 0; bottom: 0; width: 100%; height: 14px;
  }

  /* Business cards */
  .card {
    position: absolute; top: 620px;
    width: 256px; height: 420px;
    border-radius: 14px;
    box-shadow: 0 3px 10px rgba(0,0,0,.18);
  }
  .card--front { left: 112px; background: var(--paper); text-align: center; }
  .card--back { left: 395px; background: var(--card-dark); }

  .card__brand {
    position: absolute; left: 0; right: 0; top: 92px;
    font-weight: 900; font-size: 24px; line-height: 1.05;
    color: var(--orange);
  }
  .card__name {
    position: absolute; left: 0; right: 0; top: 196px;
    font-weight: 700; font-size: 27px; color: var(--orange);
  }
  .card__role {
    position: absolute; left: 0; right: 0; top: 232px;
    font-size: 11.5px; color: var(--text-grey);
  }
  .card__icons {
    position: absolute; left: 22px; right: 22px; top: 254px; height: 16px;
  }
  .card__details {
    position: absolute; left: 0; right: 0; top: 278px;
    font-size: 12.5px; line-height: 1.42; font-style: normal; color: var(--text-grey);
  }
  .card__rule {
    width: 168px; height: 1px; margin: 8px auto;
    background: var(--rule-red);
  }
  .card__back-brand {
    position: absolute; left: 0; right: 0; top: 250px;
    text-align: center; font-weight: 900; font-size: 17px;
    color: var(--orange);
  }
  .card__abn {
    position: absolute; left: 0; right: 0; bottom: 60px;
    text-align: center; font-size: 13px; color: #ffffff;
  }
</style>
</head>
<body>

<section class="letterhead" aria-label="Letterhead">
  <div class="letterhead__brand">bright crew<br>hire</div>

  <address class="letterhead__contact">
    Suite 3, 42 Tamsin Court,<br>
    Marlowe Park ACT 2611<br>
    1300 582 317<br>
    0412 637 845<br>
    dana@brightcrewhire.com.au<br>
    www.brightcrewhire.com.au<br>
    <span class="abn">ABN:</span> 52 418 736 904
  </address>

  <div class="letterhead__body">
    <p>Dear Sir/Mam,</p>
    <p>Contrary to popular belief, Lorem Ipsum is not simply random text. It has roots in a piece of classical Latin literature from 45 BC, making it over 2000 years old. Alan Whitcombe, a Latin professor at Harwood College in Vermont, looked up one of the more obscure Latin words, consectetur.</p>
    <p>Lorem Ipsum comes from sections 1.10.32 and 1.10.33 of "de Finibus Bonorum et Malorum" (The Extremes of Good and Evil) by Varro, written in 45 BC. This book is a treatise on the theory of ethics, very popular during the Renaissance. The first line of Lorem Ipsum.</p>
    <p>The standard chunk of Lorem Ipsum used since the 1500s is reproduced below for those interested. Sections 1.10.32 and 1.10.33 from "de Finibus Bonorum et Malorum" by Varro are also reproduced in their exact original.</p>
    <p>The standard chunk of Lorem Ipsum used since the 1500s is reproduced below for those interested.</p>
    <p class="letterhead__signoff">Best Regards</p>
    <span class="letterhead__signature" role="img" aria-label="Handwritten signature"></span>
  </div>

  <svg class="letterhead__footer" viewBox="0 0 400 14" preserveAspectRatio="none" aria-hidden="true">
    <polygon points="0,0 290,0 300,14 0,14" fill="var(--orange)"/>
    <polygon points="296,0 400,0 400,14 306,14" fill="var(--grey)"/>
  </svg>
</section>

<section class="card card--front" aria-label="Business card front">
  <div class="card__brand">bright crew<br>hire</div>
  <div class="card__name">Dana Holt</div>
  <div class="card__role">Account Executive</div>

  <svg class="card__icons" viewBox="0 0 212 16" aria-hidden="true">
    <line x1="0" y1="8" x2="72" y2="8" stroke="var(--orange)" stroke-width="0.8"/>
    <line x1="140" y1="8" x2="212" y2="8" stroke="var(--orange)" stroke-width="0.8"/>
    <g fill="var(--orange)">
      <circle cx="80" cy="8" r="7"/><circle cx="97" cy="8" r="7"/>
      <circle cx="115" cy="8" r="7"/><circle cx="132" cy="8" r="7"/>
    </g>
    <g fill="none" stroke="#fff" stroke-width="1.1" stroke-linecap="round">
      <path d="M77 5 q0 5 6 6"/>
      <rect x="94.5" y="4" width="5" height="8" rx="1"/>
      <rect x="111" y="5" width="8" height="6"/><path d="M111 5 l4 3 l4 -3"/>
      <circle cx="132" cy="8" r="4"/><line x1="128" y1="8" x2="136" y2="8"/><ellipse cx="132" cy="8" rx="1.8" ry="4"/>
    </g>
  </svg>

  <address class="card__details">
    1300 582 317<br>
    0412 637 845<br>
    dana@brightcrewhire.com.au<br>
    www.brightcrewhire.com.au
    <div class="card__rule"></div>
    Suite 3, 42 Tamsin Court,<br>
    Marlowe Park ACT 2611
  </address>
</section>

<section class="card card--back" aria-label="Business card back">
  <div class="card__back-brand">bright crew hire</div>
  <div class="card__abn">ABN: 52 418 736 904</div>
</section>

</body>
</html>
```